Construction APP

We need to design a modern app IOS/Android where my team can create a profile with their info, (maybe share some pictures), reviews, submit time cards, show their availability, etc.

Like a taxi app but for construction. We also want to be able to assign each team member to a project manager with who they currently working. So we will also need to be able to create profiles at the Administration level.

The goal is to keep innovating the app as we grow, so we are always open to suggestions and ideas.

Industry/Entity Type

Construction

Colors
FFC000
F8CF3A
FAE287
FDF2CF
FEFAEE

Requirements
Must have
• IOS/Android APP where my team can create a profile with their info, (maybe share some pictures), reviews, submit time cards, show their availability, etc.We also want to be able to assign each team member to a project manager with who they currently working. So we will also need to be able to create profiles at the Administration level.

```html
<!DOCTYPE html>
<html lang="en">
<head>
<meta charset="UTF-8">
<title>Construction App Screens</title>
<link href="https://fonts.googleapis.com/css2?family=Inter:wght@400;500;600;700&display=swap" rel="stylesheet">
<style>
:root{
  --bg:#f4f4f4;
  --white:#ffffff;
  --ink:#1f1f1f;
  --muted:#9a9a9a;
  --faint:#c4c4c4;
  --line:#ececec;
  --header:#f8f8f8;
  --amber:#ffc000;
  --gold:#f8cf3a;
  --sand:#fae287;
  --cream:#fdf2cf;
  --ivory:#feFaee;
  --veil:#bab08e;
}
*{margin:0;padding:0;box-sizing:border-box}
html,body{width:1200px;height:1000px;overflow:hidden;background:var(--bg);font-family:'Inter',sans-serif;color:var(--ink)}
.canvas{position:relative;width:1200px;height:1000px}
.screen{position:absolute;top:113px;width:356px;height:774px;background:var(--white);border-radius:22px;overflow:hidden;box-shadow:0 8px 30px rgba(0,0,0,.06)}
.screen-1{left:28px}.screen-2{left:422px}.screen-3{left:816px}
.abs{position:absolute}
.status-time{left:21px;top:13px;font-size:15px;font-weight:600}
.status-icons{right:14px;top:15px}
.home-bar{left:121px;bottom:8px;width:115px;height:4px;border-radius:2px;background:var(--ink)}
.app-header{left:0;top:58px;width:356px;height:57px;background:var(--header);box-shadow:0 6px 12px rgba(0,0,0,.04)}
.app-header h1{position:absolute;left:17px;top:15px;font-size:23px;font-weight:700}
.burger{right:18px;top:19px}
.greeting{left:17px;top:152px;font-size:31px;font-weight:700}
.work-label{left:16px;top:250px;font-size:17px;font-weight:600}
.tab-raise{background:var(--white);box-shadow:0 -2px 8px rgba(0,0,0,.05)}
.tab{font-size:15px;border-radius:4px;display:flex;align-items:center;justify-content:center}
.tab-on{background:var(--cream);border:1px solid var(--gold);color:var(--amber);font-weight:600}
.tab-off{background:#f7f7f7;border:1px solid #e6e6e6;color:var(--faint)}
.content{left:0;top:284px;width:356px;height:458px;background:var(--white);box-shadow:0 -4px 10px rgba(0,0,0,.04);overflow:hidden}
.date{font-size:15px}.date small{font-size:12px;color:var(--muted);margin-right:3px}
.client-label{left:15px;top:40px;font-size:14px;color:var(--muted)}
.client-name{left:15px;top:60px;font-size:29px;font-weight:700}
.todo{left:15px;top:116px;width:326px;height:49px;border:1px solid var(--line);font-size:18px;font-weight:500;padding:13px 14px}
.todo svg{position:absolute;right:12px;top:11px}
.todo-text{left:27px;top:184px;width:300px;font-size:17.5px;line-height:22px}
.todo-text a{color:var(--amber);font-size:14px;text-decoration:underline}
.time-label{top:274px;font-size:14.5px;font-weight:500}
.time-box{top:309px;width:153px;height:52px;border:1px solid var(--sand);display:flex;align-items:center;justify-content:center;font-size:18px;font-weight:500}
.info-label{left:15px;top:401px;font-size:17px;font-weight:600}
.info-box{left:15px;top:437px;width:326px;height:40px;border:1px solid var(--line)}
.job{left:0;width:356px;height:82px;border-bottom:1px solid var(--cream)}
.job h3{position:absolute;left:23px;top:23px;font-size:17.5px;font-weight:600}
.job p{position:absolute;left:23px;top:52px;font-size:14px}
.job .date{position:absolute;right:12px;top:21px;color:var(--muted);font-size:16px}
.job .date small{color:var(--faint)}
.veil{left:0;top:44px;width:82px;height:696px;background:var(--veil);overflow:hidden}
.veil span{position:absolute;background:rgba(120,110,80,.35);filter:blur(5px);border-radius:4px}
.menu{left:82px;top:44px;width:274px;height:696px;background:var(--white)}
.menu-head{left:0;top:0;width:274px;height:57px;background:var(--header)}
.menu-head h2{position:absolute;left:17px;top:20px;font-size:17px;font-weight:500}
.menu-head svg{position:absolute;right:18px;top:18px}
.menu-item{left:0;width:274px;height:64px;border-bottom:1px solid #f1f1f1;font-size:17.5px;font-weight:600;padding:20px 15px}
.menu-item svg{position:absolute;right:16px;top:21px}
.cta{left:45px;top:417px;width:184px;height:45px;background:var(--amber);display:flex;align-items:center;justify-content:center;font-size:19px;font-weight:500}
.logout{left:0;width:274px;top:564px;text-align:center;font-size:16px}
.version{left:0;width:274px;top:635px;text-align:center;font-size:13px;color:#aaa;line-height:16px}
</style>
</head>
<body>
<div class="canvas">

  <!-- Screen: active work -->
  <section class="screen screen-1">
    <div class="abs status-time">9:41</div>
    <svg class="abs status-icons" width="66" height="12" viewBox="0 0 66 12"><rect x="0" y="7" width="3" height="4" rx="1" fill="#1f1f1f"/><rect x="4.5" y="5" width="3" height="6" rx="1" fill="#1f1f1f"/><rect x="9" y="3" width="3" height="8" rx="1" fill="#1f1f1f"/><rect x="13.5" y="1" width="3" height="10" rx="1" fill="#1f1f1f"/><path d="M22 4a11 11 0 0 1 15 0l-1.5 1.6a8.6 8.6 0 0 0-12 0zM25 7a6.5 6.5 0 0 1 9 0l-1.5 1.6a4.3 4.3 0 0 0-6 0zM27.8 10a2.4 2.4 0 0 1 3.4 0L29.5 11.8z" fill="#1f1f1f"/><rect x="42" y="1" width="21" height="10" rx="3" fill="none" stroke="#1f1f1f" opacity=".5"/><rect x="44" y="3" width="17" height="6" rx="1.5" fill="#1f1f1f"/><rect x="64" y="4" width="1.5" height="4" rx=".7" fill="#1f1f1f" opacity=".5"/></svg>
    <header class="abs app-header"><h1>Home</h1>
      <svg class="abs burger" width="36" height="20" viewBox="0 0 36 20"><g stroke="#1f1f1f" stroke-width="2.6" stroke-linecap="round"><line x1="2" y1="2" x2="34" y2="2"/><line x1="8" y1="10" x2="34" y2="10"/><line x1="2" y1="18" x2="34" y2="18"/></g></svg>
    </header>
    <div class="abs greeting">Hi! Dylan</div>
    <div class="abs work-label">Work</div>
    <div class="abs tab-raise" style="left:84px;top:227px;width:136px;height:60px"></div>
    <div class="abs tab tab-on" style="left:89px;top:232px;width:127px;height:39px">In progress</div>
    <div class="abs tab tab-off" style="left:239px;top:239px;width:99px;height:30px">In line</div>
    <div class="abs content">
      <div class="abs date" style="right:17px;top:12px"><small>Date:</small>14/10/2022</div>
      <div class="abs client-label">Client</div>
      <div class="abs client-name">Polyform Works Llc.</div>
      <div class="abs todo">Work To Do
        <svg width="26" height="26" viewBox="0 0 24 24"><path d="M22.7 19l-9.1-9.1c.9-2.3.4-5-1.5-6.9-2-2-5-2.4-7.4-1.3L9 6 6 9 1.6 4.7C.4 7.1.9 10.1 2.9 12.1c1.9 1.9 4.6 2.4 6.9 1.5l9.1 9.1c.4.4 1 .4 1.4 0l2.3-2.3c.5-.4.5-1.1.1-1.4z" transform="scale(-1,1) translate(-24,0)" fill="#1f1f1f"/></svg>
      </div>
      <p class="abs todo-text">The electricity installation will be replaced with a new one. <a>Read more</a></p>
      <div class="abs time-label" style="left:15px">Start time</div>
      <div class="abs time-label" style="left:186px">End time</div>
      <div class="abs time-box" style="left:15px">7:00 am</div>
      <div class="abs time-box" style="left:186px">6:00 pm</div>
      <div class="abs info-label">Info</div>
      <div class="abs info-box"><svg class="abs" style="right:22px;top:12px" width="10" height="6" viewBox="0 0 10 6"><path d="M0 6L5 0l5 6z" fill="#1f1f1f"/></svg></div>
    </div>
    <div class="abs home-bar"></div>
  </section>

  <!-- Screen: queued work -->
  <section class="screen screen-2">
    <div class="abs status-time">9:41</div>
    <svg class="abs status-icons" width="66" height="12" viewBox="0 0 66 12"><rect x="0" y="7" width="3" height="4" rx="1" fill="#1f1f1f"/><rect x="4.5" y="5" width="3" height="6" rx="1" fill="#1f1f1f"/><rect x="9" y="3" width="3" height="8" rx="1" fill="#1f1f1f"/><rect x="13.5" y="1" width="3" height="10" rx="1" fill="#1f1f1f"/><path d="M22 4a11 11 0 0 1 15 0l-1.5 1.6a8.6 8.6 0 0 0-12 0zM25 7a6.5 6.5 0 0 1 9 0l-1.5 1.6a4.3 4.3 0 0 0-6 0zM27.8 10a2.4 2.4 0 0 1 3.4 0L29.5 11.8z" fill="#1f1f1f"/><rect x="42" y="1" width="21" height="10" rx="3" fill="none" stroke="#1f1f1f" opacity=".5"/><rect x="44" y="3" width="17" height="6" rx="1.5" fill="#1f1f1f"/><rect x="64" y="4" width="1.5" height="4" rx=".7" fill="#1f1f1f" opacity=".5"/></svg>
    <header class="abs app-header"><h1>Home</h1>
      <svg class="abs burger" width="36" height="20" viewBox="0 0 36 20"><g stroke="#1f1f1f" stroke-width="2.6" stroke-linecap="round"><line x1="2" y1="2" x2="34" y2="2"/><line x1="8" y1="10" x2="34" y2="10"/><line x1="2" y1="18" x2="34" y2="18"/></g></svg>
    </header>
    <div class="abs greeting">Hi! Dylan</div>
    <div class="abs work-label">Work</div>
    <div class="abs tab tab-off" style="left:90px;top:240px;width:104px;height:34px">In progress</div>
    <div class="abs tab-raise" style="left:208px;top:227px;width:136px;height:60px"></div>
    <div class="abs tab tab-on" style="left:214px;top:234px;width:125px;height:41px">In line</div>
    <div class="abs content">
      <div class="abs job" style="top:0"><h3>Bravtec</h3><p>Short description of the work..</p><div class="date"><small>Date:</small> 20/11/2022</div></div>
      <div class="abs job" style="top:82px"><h3>Corlano</h3><p>Short description of the work..</p><div class="date"><small>Date:</small> 24/11/2022</div></div>
      <div class="abs job" style="top:164px"><h3>Vesmark</h3><p>Short description of the work..</p><div class="date"><small>Date:</small> 28/11/2022</div></div>
      <div class="abs job" style="top:246px"><h3>Client Name</h3><p>Short description of the work..</p><div class="date"><small>Date:</small> 4/12/2022</div></div>
      <div class="abs job" style="top:328px"><h3>Ridge&amp;Co.</h3><p>Short description of the work..</p><div class="date"><small>Date:</small> 7/12/2022</div></div>
      <div class="abs job" style="top:410px"><h3>NorthBay Llc.</h3><p>Short description of the work..</p><div class="date"><small>Date:</small> 15/12/2022</div></div>
    </div>
    <div class="abs home-bar"></div>
  </section>

  <!-- Screen: side menu -->
  <section class="screen screen-3">
    <div class="abs status-time">9:41</div>
    <svg class="abs status-icons" width="66" height="12" viewBox="0 0 66 12"><rect x="0" y="7" width="3" height="4" rx="1" fill="#1f1f1f"/><rect x="4.5" y="5" width="3" height="6" rx="1" fill="#1f1f1f"/><rect x="9" y="3" width="3" height="8" rx="1" fill="#1f1f1f"/><rect x="13.5" y="1" width="3" height="10" rx="1" fill="#1f1f1f"/><path d="M22 4a11 11 0 0 1 15 0l-1.5 1.6a8.6 8.6 0 0 0-12 0zM25 7a6.5 6.5 0 0 1 9 0l-1.5 1.6a4.3 4.3 0 0 0-6 0zM27.8 10a2.4 2.4 0 0 1 3.4 0L29.5 11.8z" fill="#1f1f1f"/><rect x="42" y="1" width="21" height="10" rx="3" fill="none" stroke="#1f1f1f" opacity=".5"/><rect x="44" y="3" width="17" height="6" rx="1.5" fill="#1f1f1f"/><rect x="64" y="4" width="1.5" height="4" rx=".7" fill="#1f1f1f" opacity=".5"/></svg>
    <div class="abs veil">
      <span style="left:16px;top:22px;width:70px;height:16px"></span>
      <span style="left:16px;top:134px;width:70px;height:24px"></span>
      <span style="left:16px;top:220px;width:36px;height:14px"></span>
    </div>
    <nav class="abs menu">
      <div class="abs menu-head"><h2>MENU</h2>
        <svg width="20" height="20" viewBox="0 0 20 20"><path d="M2 2l16 16M18 2L2 18" stroke="#1f1f1f" stroke-width="2.4" stroke-linecap="round"/></svg>
      </div>
      <div class="abs menu-item" style="top:57px">Home
        <svg width="20" height="20" viewBox="0 0 24 24"><path d="M10 20v-6h4v6h5v-8h3L12 3 2 12h3v8z" fill="#1f1f1f"/></svg></div>
      <div class="abs menu-item" style="top:121px">Profile
        <svg width="22" height="22" viewBox="0 0 24 24"><circle cx="12" cy="12" r="10" fill="none" stroke="#1f1f1f" stroke-width="2"/><circle cx="12" cy="9.5" r="3.5" fill="#1f1f1f"/><path d="M5.5 18.5c1.5-2.4 4-3.5 6.5-3.5s5 1.1 6.5 3.5" fill="none" stroke="#1f1f1f" stroke-width="2"/></svg></div>
      <div class="abs menu-item" style="top:185px">Settings
        <svg width="21" height="21" viewBox="0 0 24 24"><path d="M19.4 13a7.7 7.7 0 0 0 0-2l2.1-1.6-2-3.5-2.5 1a7.4 7.4 0 0 0-1.7-1L15 3h-4l-.4 2.9a7.4 7.4 0 0 0-1.7 1l-2.5-1-2 3.5L6.6 11a7.7 7.7 0 0 0 0 2l-2.1 1.6 2 3.5 2.5-1a7.4 7.4 0 0 0 1.7 1L11 21h4l.4-2.9a7.4 7.4 0 0 0 1.7-1l2.5 1 2-3.5zM13 15.5a3.5 3.5 0 1 1 0-7 3.5 3.5 0 0 1 0 7z" transform="translate(-1,0)" fill="#1f1f1f"/></svg></div>
      <div class="abs cta">Your works</div>
      <div class="abs logout">Log out</div>
      <div class="abs version">Mr. Alvarez<br>V.1.1 2022</div>
    </nav>
    <div class="abs home-bar"></div>
  </section>

</div>
</body>
</html>
```